Equity, Effectiveness and Efficiency in charitable food relief sector

I am undertaking my PhD in food policy in the charitable food relief sector, specifically investigating the factors (supply, demand and capacity) that affect the introduction of nutrition policy and in turn, affect the sector's ability to achieve equity, effectiveness and efficiency.

I need a graphic device that incorporates this central idea of Equity, Effectiveness and Efficiency, and how the factors of supply, demand and capacity interact. There are sub-factors within supply (1-6), demand (7-10) and capacity (11 - 15). All these details are shown in the attached figure (Basic figure_Eq Effec Effic and factors.jpg)

This figure (Basic figure_Eq Effec Effic and factors.jpg) contains all the information I need in a graphic but I need something that is more visually appealing, and that can link the ideas in a format other than a table. The final graphic will outline how the food relief sector balances the core objectives of equity, effectiveness and efficiency with the factors (and sub-factors) of supply, demand and capacity.

```html
<!DOCTYPE html>
<html lang="en">
<head>
<meta charset="utf-8">
<title>Factors Affecting the Introduction of Nutrition Policy</title>
<link href="https://fonts.googleapis.com/css2?family=Arimo:wght@400;700&family=Roboto+Condensed:wght@700&display=swap" rel="stylesheet">
<style>
  :root {
    --bg: #ffffff;
    --title: #2e5b8c;
    --ink: #111111;
    --supply: #ff99cc;
    --supply-badge: #e8202a;
    --demand: #88c688;
    --demand-badge: #006633;
    --core-ring: #d2380c;
    --core: #eb5020;
    --capacity: #99cccc;
    --capacity-badge: #336699;
    --detail: #aae6e6;
    --white: #ffffff;
  }
  html, body {
    margin: 0;
    padding: 0;
    width: 1200px;
    height: 900px;
    overflow: hidden;
    background: var(--bg);
  }
  .canvas {
    display: block;
    width: 1200px;
    height: 900px;
    font-family: "Arimo", Arial, sans-serif;
  }
  .title {
    fill: var(--title);
    font-weight: 700;
    font-size: 27px;
  }
  .title-rule { stroke: var(--title); stroke-width: 1.5; }
  .heading {
    fill: var(--ink);
    font-weight: 700;
    font-size: 27px;
    text-decoration: underline;
  }
  .item { fill: var(--ink); font-size: 22px; }
  .item b { font-weight: 700; }
  .badge-num {
    fill: var(--white);
    font-weight: 700;
    font-size: 19px;
    text-anchor: middle;
  }
  .badge-num.large { font-size: 21px; }
  .supply-circle { fill: var(--supply); }
  .supply-badge { fill: var(--supply-badge); }
  .demand-circle { fill: var(--demand); }
  .demand-badge { fill: var(--demand-badge); }
  .core-ring { fill: var(--white); stroke: var(--core-ring); stroke-width: 9; }
  .core-circle { fill: var(--core); }
  .capacity-circle { fill: var(--capacity); }
  .capacity-badge { fill: var(--capacity-badge); }
  .detail-circle { fill: var(--detail); }
  .connector {
    fill: none;
    stroke: var(--capacity-badge);
    stroke-width: 3;
    stroke-linecap: round;
  }
  .core-text {
    fill: var(--white);
    font-weight: 700;
    text-anchor: middle;
  }
  .core-equity { font-size: 38px; }
  .core-effectiveness { font-family: "Roboto Condensed", "Arial Narrow", sans-serif; font-size: 31px; }
  .core-efficiency { font-size: 27px; }
</style>
</head>
<body>
<svg class="canvas" viewBox="0 0 1200 900" xmlns="http://www.w3.org/2000/svg">
  <!-- Title -->
  <text class="title" x="600" y="91" text-anchor="middle">FACTSORS AFFECTING THE INTRODUCTION OF NUTRITION POLICY</text>
  <line class="title-rule" x1="135" y1="95" x2="1065" y2="95"/>

  <!-- Circles -->
  <circle class="supply-circle" cx="198" cy="397" r="165"/>
  <circle class="capacity-circle" cx="673" cy="623" r="184"/>
  <circle class="detail-circle" cx="889" cy="406" r="83"/>
  <circle class="detail-circle" cx="1028" cy="644" r="142"/>
  <circle class="core-ring" cx="445" cy="462" r="126"/>
  <circle class="core-circle" cx="445" cy="462" r="113"/>
  <circle class="demand-circle" cx="576" cy="274" r="129"/>

  <!-- Core objectives -->
  <g class="core">
    <text class="core-text core-equity" x="445" y="426">EQUITY</text>
    <text class="core-text core-effectiveness" x="445" y="474">EFFECTIVENESS</text>
    <text class="core-text core-efficiency" x="445" y="516">EFFICIENCY</text>
  </g>

  <!-- Supply -->
  <g class="supply">
    <text class="heading" x="198" y="295" text-anchor="middle">SUPPLY</text>
    <circle class="supply-badge" cx="70" cy="334" r="13"/><text class="badge-num" x="70" y="341">1</text>
    <text class="item" x="90" y="342">Uncertain material supply</text>
    <circle class="supply-badge" cx="60" cy="364" r="13"/><text class="badge-num" x="60" y="371">2</text>
    <text class="item" x="79" y="372">Uncertain monetary supply</text>
    <circle class="supply-badge" cx="55" cy="396" r="13"/><text class="badge-num" x="55" y="403">3</text>
    <text class="item" x="75" y="404">Limited food supply</text>
    <circle class="supply-badge" cx="58" cy="428" r="13"/><text class="badge-num" x="58" y="435">4</text>
    <text class="item" x="77" y="436">Perishability</text>
    <circle class="supply-badge" cx="69" cy="458" r="13"/><text class="badge-num" x="69" y="465">5</text>
    <text class="item" x="88" y="466">Donor constraints</text>
    <circle class="supply-badge" cx="86" cy="486" r="13"/><text class="badge-num" x="86" y="493">6</text>
    <text class="item" x="106" y="494">Donor relationships</text>
  </g>

  <!-- Demand -->
  <g class="demand">
    <text class="heading" x="576" y="204" text-anchor="middle">DEMAND</text>
    <circle class="demand-badge" cx="476" cy="242" r="13"/><text class="badge-num" x="476" y="249">7</text>
    <text class="item" x="495" y="250">Uncertain demand</text>
    <circle class="demand-badge" cx="471" cy="275" r="13"/><text class="badge-num" x="471" y="282">8</text>
    <text class="item" x="490" y="283">Limited demand</text>
    <circle class="demand-badge" cx="476" cy="306" r="13"/><text class="badge-num" x="476" y="313">9</text>
    <text class="item" x="495" y="314">Client choice</text>
    <circle class="demand-badge" cx="491" cy="335" r="13"/><text class="badge-num" x="491" y="342" style="font-size:17px">10</text>
    <text class="item" x="515" y="343">Food wastage</text>
  </g>

  <!-- Capacity connectors -->
  <path class="connector" d="M542 586 Q548 594 558 594 L681 594 Q702 594 716 578 L824 471"/>
  <path class="connector" d="M800 429 Q810 480 866 494"/>
  <path class="connector" d="M536 679 Q545 686 556 686 L710 686 Q722 686 731 680 L772 652 Q782 645 794 645 L876 645"/>
  <path class="connector" d="M884 597 Q866 645 884 692"/>

  <!-- Capacity -->
  <g class="capacity">
    <text class="heading" x="673" y="509" text-anchor="middle">CAPACITY</text>
    <circle class="capacity-badge" cx="539" cy="571" r="16"/><text class="badge-num large" x="539" y="579">11</text>
    <text class="item" x="564" y="579">Storage:</text>
    <circle class="capacity-badge" cx="530" cy="624" r="16"/><text class="badge-num large" x="530" y="632">12</text>
    <text class="item" x="554" y="632">Transportation</text>
    <circle class="capacity-badge" cx="536" cy="666" r="16"/><text class="badge-num large" x="536" y="674">13</text>
    <text class="item" x="560" y="674">Workforce:</text>
    <circle class="capacity-badge" cx="559" cy="713" r="16"/><text class="badge-num large" x="559" y="721">14</text>
    <text class="item" x="584" y="721">External stakeolders</text>
    <circle class="capacity-badge" cx="592" cy="748" r="16"/><text class="badge-num large" x="592" y="756">15</text>
    <text class="item" x="617" y="756">Budget</text>
  </g>

  <!-- Storage detail -->
  <g class="storage-detail">
    <text class="item" x="819" y="398"><tspan font-weight="700">a</tspan>) Cold</text>
    <text class="item" x="819" y="426"><tspan font-weight="700">b</tspan>) Warehouse</text>
  </g>

  <!-- Workforce detail -->
  <g class="workforce-detail">
    <text class="item" x="920" y="592"><tspan font-weight="700">a</tspan>) Volunteers</text>
    <text class="item" x="911" y="620"><tspan font-weight="700">b</tspan>) Expertise</text>
    <text class="item" x="906" y="649"><tspan font-weight="700">c</tspan>) Attitudes and Beliefs</text>
    <text class="item" x="910" y="677"><tspan font-weight="700">d</tspan>) Collaboration</text>
    <text class="item" x="920" y="706"><tspan font-weight="700">e</tspan>) Executive Support</text>
  </g>
</svg>
</body>
</html>
```